DMR Property - Business Cards

Looking for a business card & general letterhead, signage etc design for our new logo.

Colours:
000a20
0056a2
00b5ef
0088ce
68cef2

Fonts:
Poppins
Karla

Please keep look and feel of new brand - example in the zip package I sent.

```html
<!DOCTYPE html>
<html lang="en">
<head>
<meta charset="utf-8">
<title>DMR Property – Business Cards</title>
<link href="https://fonts.googleapis.com/css2?family=Poppins:wght@400;600;700&family=Karla:wght@400;500&display=swap" rel="stylesheet">
<style>
  :root {
    --navy: #000a20;
    --navy-card: #0e1428;
    --blue: #0056a2;
    --mid-blue: #0088ce;
    --cyan: #00b5ef;
    --light-blue: #68cef2;
    --white: #ffffff;
    --ink: #3a3a3a;
    --backdrop: #3e3e3e;
    --emboss: #2a3670;
    --emboss-dark: #1a2244;
  }
  * { margin: 0; padding: 0; box-sizing: border-box; }
  html, body { width: 1200px; height: 803px; overflow: hidden; background: var(--backdrop); }
  .canvas { position: relative; width: 1200px; height: 803px; }

  .card {
    position: absolute;
    top: 258px;
    width: 500px;
    height: 286px;
    border-radius: 18px;
    overflow: hidden;
    border-bottom: 3px solid var(--light-blue);
  }
  .card-front { left: 70px; background: var(--white); }
  .card-back { left: 630px; background: var(--navy-card); }

  .front-band { position: absolute; inset: 0; width: 100%; height: 100%; }

  .holder {
    position: absolute; left: 26px; top: 128px;
    color: var(--white); font-family: "Poppins", sans-serif;
  }
  .holder-name { font-size: 20px; font-weight: 700; line-height: 1.15; white-space: nowrap; }
  .holder-title { font-family: "Karla", sans-serif; font-size: 13px; font-weight: 500; }

  .address {
    position: absolute; right: 28px; top: 26px; text-align: right; font-style: normal;
    font-family: "Karla", sans-serif; font-size: 12.5px; line-height: 1.35; color: var(--ink);
  }
  .contacts {
    position: absolute; right: 26px; top: 118px; list-style: none;
    font-family: "Karla", sans-serif; font-size: 12px; line-height: 1.45; color: var(--ink);
  }
  .contacts li { display: flex; justify-content: flex-end; align-items: center; gap: 6px; }
  .contacts svg { width: 10px; height: 10px; fill: var(--blue); }

  .brand {
    position: absolute; display: flex; align-items: center; gap: 10px;
    font-family: "Poppins", sans-serif; font-weight: 700; white-space: nowrap;
  }
  .brand-dot { border-radius: 50%; flex: none; }
  .brand-front { left: 236px; bottom: 44px; font-size: 28px; color: var(--blue); }
  .brand-front .brand-dot { width: 20px; height: 20px; background: var(--light-blue); }
  .brand-back { left: 50%; top: 50%; transform: translate(-50%, -50%); font-size: 44px; color: var(--emboss); }
  .brand-back .brand-dot { width: 30px; height: 30px; background: var(--emboss-dark); }
</style>
</head>
<body>
<main class="canvas">
  <section class="card card-front" aria-label="Business card front">
    <svg class="front-band" viewBox="0 0 500 286" preserveAspectRatio="none" aria-hidden="true">
      <path d="M0 0 H255 C205 90 210 220 125 286 H0 Z" fill="var(--light-blue)"/>
      <path d="M0 0 H243 C193 90 198 220 113 286 H0 Z" fill="var(--white)"/>
      <path d="M0 0 H236 C186 90 191 220 106 286 H0 Z" fill="var(--blue)"/>
    </svg>
    <div class="holder">
      <p class="holder-name">Alex Morgan</p>
      <p class="holder-title">President</p>
    </div>
    <address class="address">1520 Maple Crescent<br>Halden, Canada 20418</address>
    <ul class="contacts">
      <li>555-210-4837 <svg viewBox="0 0 10 10"><path d="M2 0h2l1 3-1.5 1a6 6 0 0 0 2.5 2.5L7 5l3 1v2c0 1-1 2-2 2A8 8 0 0 1 0 2c0-1 1-2 2-2z"/></svg></li>
      <li>555-210-6391 <svg viewBox="0 0 10 10"><path d="M2 0h6v10H2zM3 1v7h4V1z"/></svg></li>
      <li>info@dmrproperty.com <svg viewBox="0 0 10 10"><path d="M0 2h10v6H0zM1 3l4 3 4-3"/></svg></li>
      <li>www.dmrproperty.com <svg viewBox="0 0 10 10"><circle cx="5" cy="5" r="5"/></svg></li>
    </ul>
    <div class="brand brand-front"><span class="brand-dot"></span>DMR Property</div>
  </section>

  <section class="card card-back" aria-label="Business card back">
    <div class="brand brand-back"><span class="brand-dot"></span>DMR Property</div>
  </section>
</main>
</body>
</html>
```